Travel video blogger needs website design

I need a website designed for my new travel video blog "Roaming Sparrow". I have only just started but need a website that is fairly simple and not too busy. I have a logo which I want on it (I have attached it to this project). I also want a link to all my other social medias on the main page (vidtrekhub, Snapwell and Palnook) and my videos as well. Here is a link to my vidtrekhub page for you to look at: https://www.vidtrekhub.net/channel/QRm4tZ8pWnE2HX57YKccd31v
As I have only just started and I am still trying to find my specific niche, again I need it to be sleek and simple that I can go in and change slightly here and there. I would like these pages on the website: About Me, Videos, Social Media, Blog, Gallery, contact me. for an example I like the look of www.theroamingkinfolk.net website.

I already have the domain and I am with Harborweb with pagecraftr.org. I just want to spend my time getting better and learning about videos then trying to create a website (I am a bit of a perfectionist when I try to do something).

Target Market(s)

Young Adults (majority females) between the ages of 18 and 30 with an interest in travelling.

Industry/Entity Type

Travel Industry

Number of Pages Required

1 page

Colors

Designer to choose colors to be used in the design.

Requirements
Must have
• A like to my Snapwell, Palnook and vidtrekhub channels on the home page
• Must be a nice, simple design
• Must have my logo on the front and name "Roaming Sparrow"
Nice to have
• A nice light, bright coloured theme
Should not have
• A dark coloured theme

```html
<!DOCTYPE html>
<html lang="en">
<head>
<meta charset="utf-8">
<title>Roaming Sparrow</title>
<link href="https://fonts.googleapis.com/css2?family=Lora:wght@400&family=Arimo:wght@400&display=swap" rel="stylesheet">
<style>
  :root {
    --page-bg: #fcfaf7;
    --hero-bg: #f6ece0;
    --card-bg: #ffffff;
    --ink: #1f1d1b;
    --body-text: #5f5c59;
    --accent: #d8b584;
    --photo-party-a: #d9cdb5;
    --photo-party-b: #7f9a62;
    --photo-trail-a: #4f5a52;
    --photo-trail-b: #a9a59a;
  }
  * { margin: 0; padding: 0; box-sizing: border-box; }
  html, body { width: 1200px; height: 700px; overflow: hidden; }
  body {
    background: var(--page-bg);
    position: relative;
    font-family: "Arimo", Arial, sans-serif;
    color: var(--body-text);
  }
  .hero { position: absolute; left: 0; top: 42px; width: 1200px; height: 268px; }
  .hero-intro {
    position: absolute; left: 0; top: 0; width: 600px; height: 268px;
    background: var(--hero-bg);
  }
  .brand {
    position: absolute; left: 270px; top: 40px; width: 286px;
    display: flex; align-items: center; justify-content: center; gap: 8px;
    font-family: "Lora", Georgia, serif; font-size: 15px; color: var(--ink);
  }
  .brand-dot { width: 10px; height: 10px; border-radius: 50%; background: var(--ink); }
  .hero-title {
    position: absolute; left: 270px; top: 93px; width: 286px; text-align: center;
    font-family: "Lora", Georgia, serif; font-weight: 400; font-size: 22px; color: var(--ink);
  }
  .hero-text {
    position: absolute; left: 266px; top: 130px; width: 294px; text-align: center;
    font-size: 11.3px; line-height: 17px;
  }
  .btn {
    position: absolute; left: 358px; top: 198px; width: 112px; height: 33px;
    background: var(--card-bg); box-shadow: 0 2px 6px rgba(0,0,0,0.12);
    display: flex; align-items: center; justify-content: center;
    font-family: "Lora", Georgia, serif; font-size: 12.5px; color: var(--ink);
  }
  .hero-photo {
    position: absolute; left: 600px; top: 0; width: 600px; height: 268px;
    background: linear-gradient(120deg, var(--photo-party-a) 0%, #eadbc9 45%, var(--photo-party-b) 100%);
  }
  .story { position: absolute; left: 0; top: 0; }
  .story-frame {
    position: absolute; left: 222px; top: 388px; width: 295px; height: 283px;
    border: 2px solid var(--accent);
  }
  .story-photo {
    position: absolute; left: 234px; top: 376px; width: 295px; height: 283px;
    background: linear-gradient(180deg, var(--photo-trail-a) 0%, #3e5a3a 45%, var(--photo-trail-b) 100%);
  }
  .story-head {
    position: absolute; left: 474px; top: 399px; width: 360px; height: 101px;
    background: var(--card-bg); padding: 15px 17px;
  }
  .story-tag { font-size: 10px; letter-spacing: 0.3px; color: var(--accent); margin-left: 2px; }
  .story-title {
    font-family: "Lora", Georgia, serif; font-weight: 400; font-size: 17.5px;
    line-height: 25px; color: var(--ink); margin-top: 6px;
  }
  .story-body {
    position: absolute; left: 581px; top: 525px; width: 384px; height: 145px;
    background: var(--card-bg); padding: 18px 25px;
    font-size: 11.3px; line-height: 17px;
  }
  .read-more {
    display: inline-block; margin-top: 7px;
    font-family: "Lora", Georgia, serif; font-size: 12.5px; color: var(--ink);
    text-decoration: underline;
  }
</style>
</head>
<body>
  <section class="hero">
    <div class="hero-intro">
      <div class="brand"><span class="brand-dot"></span>Roaming Sparrow</div>
      <h1 class="hero-title">Welcome to my Family!</h1>
      <p class="hero-text">Lorem ipsum dolor sit amet, consectetur adipiscing elit. Sed pharetra dignissim nunc vehicula tincidunt. Praesent nec nisl varius velit tempus sagittis at in tellus.</p>
      <a class="btn">Learn More</a>
    </div>
    <div class="hero-photo" role="img" aria-label="Photo of friends raising glasses in a toast outdoors among green trees"></div>
  </section>

  <section class="story">
    <div class="story-frame"></div>
    <div class="story-photo" role="img" aria-label="Photo of a traveller with a backpack walking a rocky mountain trail"></div>
    <div class="story-head">
      <p class="story-tag">ADVENTURE</p>
      <h2 class="story-title">Lorem ipsum dolor sit amet, consectetur adipiscing elit.</h2>
    </div>
    <div class="story-body">
      <p>Etiam consectetur in metus in pellentesque. Proin at rhoncus dui. Donec dapibus est et libero ornare pulvinar. Cras eu molestie nunc, ut molestie sapien. Nunc vestibulum, nunc vitae elementum faucibus, ipsum neque efficitur metus, et mollis arcu nisl ut tortor. Etiam sed auctor ante.</p>
      <a class="read-more">Read More</a>
    </div>
  </section>
</body>
</html>
```